Civic Holdwell Business Card

We are looking to design new business cards for our company. We have two office locations and would like to have both full addresses on the card. Each address needs two lines for the building name and street address and a line or two for the city, state and zip code. There should be a place for 2-3 phone numbers. The addresses and phone numbers are at the bottom of this description. We also need a place to put our company website and one email address. Our logo is attached.
We would like the card to be two sided. The back of the card should have a blue background with some part of our logo design on it. We would like the full logo on the front of the card as well. The front of the card should have a white background with the blue logo. We are open to listing our addresses on the front or the back of the card. The person who designed our logo gave us an excellent business card idea that we really liked. I have attached a picture of his business card idea so that we can build off of it.
Addresses:
The Tanner Hall
2184 17th Street NW
Washington, DC 20007
Marlow Crest Tower
410 Dorsen Avenue #2215
Miami, FL 33131
Phone Numbers: (202) 555-0148
(202) 555-0193
Website: www.civicholdwell.example

```html
<!DOCTYPE html>
<html lang="en">
<head>
<meta charset="utf-8">
<title>Civic Holdwell Business Card</title>
<link rel="stylesheet" href="https://fonts.googleapis.com/css2?family=Open+Sans:wght@400;500&display=swap">
<style>
  :root {
    --brand-blue: #2a327d;
    --card-white: #ffffff;
    --backdrop: #d6d6d6;
    --ink: #2a327d;
  }
  * { box-sizing: border-box; margin: 0; padding: 0; }
  html, body {
    width: 1200px;
    height: 900px;
    overflow: hidden;
  }
  body {
    background: var(--backdrop);
    font-family: "Open Sans", Verdana, sans-serif;
    display: flex;
    align-items: center;
    justify-content: center;
    gap: 40px;
  }
  .card {
    position: relative;
    width: 540px;
    height: 309px;
    overflow: hidden;
    box-shadow: 0 6px 18px rgba(0, 0, 0, 0.18);
  }

  /* Wordmark */
  .wordmark {
    display: flex;
    align-items: center;
    gap: 12px;
  }
  .wordmark-square {
    width: 40px;
    height: 40px;
    border-radius: 4px;
    flex: none;
  }
  .wordmark-name {
    font-size: 30px;
    font-weight: 400;
    letter-spacing: 0.06em;
    text-transform: uppercase;
    line-height: 1;
  }

  /* Back side */
  .card-back {
    background: var(--brand-blue);
  }
  .card-back .bottom-band {
    position: absolute;
    left: 0;
    bottom: 0;
    width: 100%;
    height: 22px;
    background: var(--card-white);
  }
  .card-back .wordmark {
    position: absolute;
    top: 118px;
    left: 50%;
    transform: translateX(-50%);
    color: var(--card-white);
  }
  .card-back .wordmark-square { background: var(--card-white); }

  /* Front side */
  .card-front {
    background: var(--card-white);
    color: var(--ink);
  }
  .card-front .top-band {
    position: absolute;
    top: 0;
    left: 0;
    width: 100%;
    height: 14px;
    background: var(--brand-blue);
  }
  .card-front .wordmark {
    position: absolute;
    top: 64px;
    left: 50%;
    transform: translateX(-50%);
    color: var(--ink);
  }
  .card-front .wordmark-square { background: var(--brand-blue); }
  .website {
    position: absolute;
    top: 148px;
    width: 100%;
    text-align: center;
    font-size: 13px;
    font-weight: 500;
  }
  .office {
    position: absolute;
    font-size: 12px;
    line-height: 1.35;
    font-style: normal;
  }
  .office-miami {
    left: 26px;
    top: 186px;
  }
  .office-dc {
    right: 26px;
    top: 214px;
    text-align: right;
  }
</style>
</head>
<body>

  <section class="card card-back" aria-label="Card back">
    <div class="wordmark">
      <span class="wordmark-square"></span>
      <span class="wordmark-name">Civic Holdwell</span>
    </div>
    <div class="bottom-band"></div>
  </section>

  <section class="card card-front" aria-label="Card front">
    <div class="top-band"></div>
    <div class="wordmark">
      <span class="wordmark-square"></span>
      <span class="wordmark-name">Civic Holdwell</span>
    </div>
    <p class="website">www.civicholdwell.example</p>
    <address class="office office-miami">
      Marlow Crest Tower<br>
      410 Dorsen Avenue #2215<br>
      Miami, FL 33131<br>
      (202) 555-0193
    </address>
    <address class="office office-dc">
      The Tanner Hall<br>
      2184 17th Street NW<br>
      Washington, DC 20007<br>
      (202) 555-0148
    </address>
  </section>

</body>
</html>
```